Employee I.D. Card - Badge

We need an employee I.D. card designed. Our employees are going to be wearing these. I would like to have it look nice. Something professional yet cool (not uptight if that makes sense).
Project Scope:
Vertical orientation
Company name ------------- (Bright and Tidy)
Website ------------- (brightandtidymn.example)
Employee Picture
background check image
front and back designed - same design on either side
You can create the card without having the employee images on them.
Here are the dimensions -
2.125 x 3.370 inches
Double sided - same design can be used front and back
Background badge - I would like to add an image that shows that the employee has taken a background check. I've added the press-kit for the company we use. If you have a better idea than incorporating their logo, we can certainly do something different.
Example image-
https://www.lookupzone.example/find?q=background+check+badge&kind=images&ref=XyZ4qWm82LpRt:
The print company will set up the names.
Logo is attached
Also attached are our business cards. You can use this for an idea of brand/company style.
Our website - brightandtidymn.example

```html
<!DOCTYPE html>
<html lang="en">
<head>
<meta charset="utf-8">
<title>Bright and Tidy – Employee ID Badge</title>
<link rel="stylesheet" href="https://fonts.googleapis.com/css2?family=Work+Sans:wght@400;500&display=swap">
<style>
  :root {
    --page-bg: #dfe1e1;
    --card-bg: #ffffff;
    --band-start: #0b78c1;
    --band-end: #08aae8;
    --band-text: #ffffff;
    --brand-blue: #1a8fd0;
    --seal-fill: #d4e6f2;
    --photo-top: #ece4df;
    --photo-mid: #8c7f78;
    --photo-low: #3b3c3d;
  }
  * { margin: 0; padding: 0; box-sizing: border-box; }
  html, body {
    width: 1200px;
    height: 992px;
    overflow: hidden;
    background: var(--page-bg);
    font-family: "Work Sans", Arial, sans-serif;
  }
  .sheet {
    position: relative;
    width: 1200px;
    height: 992px;
  }
  .badge-card {
    position: absolute;
    top: 158px;
    width: 425px;
    height: 676px;
    background: var(--card-bg);
    box-shadow: 0 6px 24px rgba(0, 0, 0, 0.18);
    overflow: hidden;
  }
  .badge-card--front { left: 143px; }
  .badge-card--back { left: 629px; }

  .employee-photo {
    position: absolute;
    left: 50px;
    top: 27px;
    width: 342px;
    height: 442px;
    border-radius: 150px 150px 0 0;
    background: linear-gradient(180deg, var(--photo-top) 0%, var(--photo-mid) 38%, var(--photo-low) 62%, var(--photo-low) 100%);
  }

  .web-band {
    position: absolute;
    left: 0;
    top: 469px;
    width: 100%;
    height: 58px;
    background: linear-gradient(90deg, var(--band-start), var(--band-end));
    display: flex;
    align-items: center;
    justify-content: flex-end;
    padding-right: 36px;
  }
  .web-address {
    color: var(--band-text);
    font-size: 21px;
    font-weight: 400;
    letter-spacing: 0.3px;
    white-space: nowrap;
  }

  .brand-name {
    position: absolute;
    left: 38px;
    top: 592px;
    display: flex;
    align-items: center;
    gap: 8px;
    color: var(--brand-blue);
    font-size: 27px;
    font-weight: 500;
    line-height: 1;
    white-space: nowrap;
  }
  .brand-dot {
    width: 10px;
    height: 10px;
    border-radius: 50%;
    background: var(--brand-blue);
  }

  .check-seal {
    position: absolute;
    left: 301px;
    top: 567px;
    width: 83px;
    height: 83px;
    border-radius: 50%;
    background: var(--seal-fill);
  }
</style>
</head>
<body>
<main class="sheet">
  <section class="badge-card badge-card--front" aria-label="Employee ID card, front">
    <div class="employee-photo" role="img" aria-label="Employee portrait photo"></div>
    <div class="web-band"><span class="web-address">www.brightandtidymn.example</span></div>
    <div class="brand-name"><span class="brand-dot"></span>Bright and Tidy</div>
    <div class="check-seal" role="img" aria-label="Background check seal"></div>
  </section>

  <section class="badge-card badge-card--back" aria-label="Employee ID card, back">
    <div class="employee-photo" role="img" aria-label="Employee portrait photo"></div>
    <div class="web-band"><span class="web-address">www.brightandtidymn.example</span></div>
    <div class="brand-name"><span class="brand-dot"></span>Bright and Tidy</div>
    <div class="check-seal" role="img" aria-label="Background check seal"></div>
  </section>
</main>
</body>
</html>
```